Travertine Marketing Postcard

We have brought quality pool building materials to our customers since 2000. We want our current customers and prospects to see concisely in a post card that we have premium/select travertine coping and pavers as well in stock at great prices. We can deliver the same quality product and service to them with the travertine as we have with our ceramic swimming pool tile. We want them to know that they can call us for a quote. We want them to know that in addition to pricing that is more than competitive, we are offering special freight rates and get the product to them in two business days.
Updates

Reason: I need more time to revise and decide.

Industry/Entity Type

Building

Requirements
Must have
• The quality of the product is premium /select. There are 8 colors and the most popular sizes. Even though the product is coming from GA we are offering special freight rates and in some cases can get the product to their project quicker than the local supplier. Orders received by 2:00PM EST can be shipped same day and received in two days. Outstanding customer service.

```html
<!DOCTYPE html>
<html lang="en">
<head>
<meta charset="utf-8">
<title>Heritage Pool Stone – Travertine Postcard</title>
<link rel="stylesheet" href="https://fonts.googleapis.com/css2?family=Cormorant+Garamond:ital,wght@1,500&family=Roboto+Condensed:wght@400&family=Encode+Sans+Condensed:wght@400;700&display=swap">
<style>
  :root{
    --page:#ffffff;
    --frame:#f1dfae;
    --cream:#efece2;
    --cream-light:#f7f5ee;
    --gold:#a98b4c;
    --gold-line:#c9a862;
    --blue:#2b98cf;
    --ink:#2d2a26;
    --stone-1:#b9b0a1;
    --stone-2:#d6cfc2;
    --pool-1:#3fa9dc;
    --pool-2:#1d84c2;
  }
  *{margin:0;padding:0;box-sizing:border-box}
  html,body{width:1200px;height:930px;overflow:hidden;background:var(--page)}
  .postcard{position:relative;width:1200px;height:930px;background:var(--page)}
  .card{
    position:absolute;left:24px;top:24px;width:1152px;height:882px;
    border:4px solid var(--frame);border-radius:8px;overflow:hidden;
    background:radial-gradient(ellipse at 40% 30%,var(--cream-light),var(--cream) 70%);
  }
  .scene{position:absolute;left:0;top:0;width:1152px;height:882px}
  .brand-box{
    position:absolute;left:320px;top:8px;width:556px;height:148px;background:#fff;
    display:flex;align-items:center;justify-content:center;gap:14px;
  }
  .brand-mark{width:14px;height:14px;background:var(--gold)}
  .brand-name{
    font-family:"Roboto Condensed",sans-serif;font-weight:400;font-size:42px;
    color:var(--gold);white-space:nowrap;
  }
  .offer{
    position:absolute;left:0;top:186px;width:1152px;text-align:center;
    font-family:"Roboto Condensed",sans-serif;
  }
  .headline{
    font-family:"Cormorant Garamond",serif;font-style:italic;font-weight:500;
    color:var(--blue);font-size:36px;line-height:56px;
  }
  .headline .grade{color:var(--gold);font-size:50px}
  .point{font-size:27px;line-height:54px;color:var(--gold);white-space:nowrap}
  .point .accent{color:var(--blue)}
  .point .warm{color:var(--gold)}
  .point.blue{color:var(--blue)}
  .contact{
    position:absolute;left:22px;top:690px;
    font-family:"Encode Sans Condensed",sans-serif;color:var(--ink);
  }
  .contact p{font-size:27px;line-height:40px;white-space:nowrap}
  .contact .phones{font-size:22px;font-weight:700;line-height:40px}
  .contact .phones span{margin-right:30px}
</style>
</head>
<body>
<div class="postcard">
  <div class="card">
    <svg class="scene" viewBox="0 0 1152 882" role="img" aria-label="Photo of a travertine paver pool deck with steps at left and blue pool water at right">
      <defs>
        <linearGradient id="deck" x1="0" y1="0" x2="1" y2="0">
          <stop offset="0" stop-color="var(--stone-1)"/>
          <stop offset="0.35" stop-color="var(--stone-2)"/>
          <stop offset="0.62" stop-color="var(--stone-2)"/>
          <stop offset="0.72" stop-color="var(--pool-1)"/>
          <stop offset="1" stop-color="var(--pool-2)"/>
        </linearGradient>
      </defs>
      <path d="M0,350 C200,560 500,660 760,630 C930,610 1060,560 1152,512 L1152,882 L0,882 Z" fill="url(#deck)"/>
      <path d="M0,350 C200,560 500,660 760,630 C930,610 1060,560 1152,512" fill="none" stroke="var(--gold-line)" stroke-width="7"/>
    </svg>

    <div class="brand-box">
      <span class="brand-mark"></span>
      <span class="brand-name">Heritage Pool Stone</span>
    </div>

    <div class="offer">
      <h1 class="headline"><span class="grade">premium/select</span> travertine coping and pavers</h1>
      <p class="point"><span class="accent">8 colors</span> and the most popular sizes</p>
      <p class="point blue">the same quality product and service as ceramic swimming pool tile</p>
      <p class="point">competitive price &amp; special freight rates</p>
      <p class="point blue">Order by 2:00PM for same day <span class="warm">shipping and receiving</span> in two days</p>
    </div>

    <div class="contact">
      <p>4210 Meadow Ridge Ct. Lakeview, GA 30000</p>
      <p>www.heritagepoolstone.com</p>
      <p>Email: hello@heritagepoolstone.com</p>
      <p class="phones"><span>Phone: 555-014-2288</span><span>Toll Free: 800-555-0147</span>Fax: 555-014-2265</p>
    </div>
  </div>
</div>
</body>
</html>
```